Edgy rebranded biz cards QBL

We are rebranding our 20 yr old mortgage company with a new logo and would like cards to compliment our new look.

Target Market(s)

potential home buyers or clients for refinance

Industry/Entity Type

Mortgage Brokerage

Contact Information for Business Card

418 W. Tamsin Rd #340
Henderson, NV 89152
702.481.5927 o
702-481-5920 f
www.quarrybluelend,com
nmls 612084
QBL is an equal housing lender

Font styles to use
Sans Serif

Colors
0455a3
3176b5
0393ce
33a6d7

Requirements
Must have
• space for a photo
Nice to have
• One side with the company info and the other with the person's info

```html
<!DOCTYPE html>
<html lang="en">
<head>
<meta charset="utf-8">
<title>Quarry Blue Lending – Business Card</title>
<link rel="stylesheet" href="https://fonts.googleapis.com/css2?family=Montserrat:wght@400;500;600;700&display=swap">
<style>
  :root {
    --page-bg: #f5f5f5;
    --card-white: #ffffff;
    --brand-blue: #0677bc;
    --logo-blue: #0a72bb;
    --blue-deep: #2f6db5;
    --blue-light: #3f86c6;
    --silver-light: #e6e7e9;
    --silver-dark: #8f9095;
    --text-light: #ffffff;
  }
  * { box-sizing: border-box; margin: 0; padding: 0; }
  html, body {
    width: 1200px;
    height: 1200px;
    overflow: hidden;
    background: var(--page-bg);
    font-family: "Montserrat", sans-serif;
  }
  .canvas { position: relative; width: 1200px; height: 1200px; }

  .card {
    position: absolute;
    width: 769px;
    height: 439px;
    overflow: hidden;
  }
  .card--front { left: 217px; top: 130px; background: var(--card-white); }
  .card--back  { left: 218px; top: 656px; background: var(--brand-blue); }

  .front-art { position: absolute; inset: 0; width: 100%; height: 100%; }

  .wordmark {
    position: absolute;
    left: 177px;
    top: 219px;
    transform: translate(-50%, -50%);
    text-align: center;
    font-weight: 700;
    font-size: 30px;
    line-height: 1.1;
    letter-spacing: 0.5px;
    text-transform: uppercase;
    white-space: nowrap;
  }
  .wordmark--front { color: var(--logo-blue); }
  .wordmark--back  { color: var(--text-light); left: 176px; }

  .divider {
    position: absolute;
    left: 345px;
    top: 99px;
    width: 2px;
    height: 241px;
    background: var(--text-light);
  }

  .contact-list { list-style: none; }
  .contact-item {
    position: absolute;
    left: 0;
    display: flex;
    align-items: center;
    color: var(--text-light);
    font-size: 21px;
    font-weight: 500;
    line-height: 1.2;
    white-space: nowrap;
  }
  .contact-icon {
    position: absolute;
    left: 387px;
    width: 26px;
    height: 26px;
    transform: translateY(-50%);
  }
  .contact-text {
    position: absolute;
    left: 426px;
    transform: translateY(-50%);
    color: var(--text-light);
    font-size: 21px;
    font-weight: 500;
    line-height: 26px;
    white-space: nowrap;
    letter-spacing: 0.2px;
  }
  .contact-text--address { line-height: 26px; }

  .silver-band {
    position: absolute;
    left: 0;
    bottom: 0;
    width: 100%;
    height: 25px;
    background: linear-gradient(90deg, var(--silver-light), var(--silver-dark));
  }
</style>
</head>
<body>
<div class="canvas">

  <section class="card card--front">
    <svg class="front-art" viewBox="0 0 1237 707" preserveAspectRatio="none" aria-hidden="true">
      <defs>
        <linearGradient id="blueFill" x1="0" y1="1" x2="1" y2="0">
          <stop offset="0" stop-color="#2f69b4"/>
          <stop offset="1" stop-color="#4087c7"/>
        </linearGradient>
        <linearGradient id="silverFill" x1="0" y1="0" x2="0" y2="1">
          <stop offset="0" stop-color="#eeeff1"/>
          <stop offset="1" stop-color="#8f9095"/>
        </linearGradient>
      </defs>
      <polygon fill="url(#blueFill)" points="427,0 963,0 696,325"/>
      <polygon fill="url(#silverFill)" points="963,0 1008,0 427,707 381,707"/>
      <polygon fill="url(#blueFill)" points="1008,0 1170,0 588,707 427,707"/>
      <polygon fill="url(#silverFill)" points="1170,0 1216,0 634,707 588,707"/>
      <polygon fill="url(#blueFill)" points="1216,0 1237,0 1237,707 634,707"/>
    </svg>
    <div class="wordmark wordmark--front">Quarry Blue<br>Lending</div>
  </section>

  <section class="card card--back">
    <div class="wordmark wordmark--back">Quarry Blue<br>Lending</div>
    <div class="divider"></div>

    <ul class="contact-list">
      <li>
        <svg class="contact-icon" style="top:157px" viewBox="0 0 24 24" aria-hidden="true">
          <path fill="#fff" d="M12 1.5a7.5 7.5 0 0 0-7.5 7.5c0 5.3 7.5 13.5 7.5 13.5s7.5-8.2 7.5-13.5A7.5 7.5 0 0 0 12 1.5zm0 10.3a2.8 2.8 0 1 1 0-5.6 2.8 2.8 0 0 1 0 5.6z"/>
        </svg>
        <span class="contact-text contact-text--address" style="top:157px">418 W Tamsin Rd #340<br>Henderson, NV 89152</span>
      </li>
      <li>
        <svg class="contact-icon" style="top:209px" viewBox="0 0 24 24" aria-hidden="true">
          <path fill="#fff" d="M6.6 2.3c.5-.3 1.1-.2 1.5.2l2.4 3c.4.5.4 1.2 0 1.7L9 8.9c1.2 2.5 3.3 4.6 5.9 5.9l1.7-1.5c.5-.4 1.2-.4 1.7 0l3 2.4c.4.4.5 1 .2 1.5l-1.4 2.4c-.4.7-1.2 1-2 .9C10 19.5 4.4 13.9 3.5 6.7c-.1-.8.2-1.6.9-2z"/>
        </svg>
        <span class="contact-text" style="top:209px">(702) 481-5927</span>
      </li>
      <li>
        <svg class="contact-icon" style="top:250px" viewBox="0 0 24 24" aria-hidden="true">
          <g fill="none" stroke="#fff" stroke-width="1.6" stroke-linejoin="round">
            <path d="M7 8V2.5h7.5L17 5v3"/>
            <rect x="2" y="8" width="20" height="8" rx="1.5"/>
          </g>
          <rect x="7" y="13" width="10" height="8.5" fill="#fff"/>
        </svg>
        <span class="contact-text" style="top:250px">(702) 481-5920</span>
      </li>
      <li>
        <svg class="contact-icon" style="top:294px" viewBox="0 0 24 24" aria-hidden="true">
          <g fill="none" stroke="#fff" stroke-width="1.5">
            <circle cx="12" cy="12" r="10"/>
            <ellipse cx="12" cy="12" rx="4.5" ry="10"/>
            <line x1="12" y1="2" x2="12" y2="22"/>
            <line x1="2" y1="12" x2="22" y2="12"/>
            <path d="M3.5 7h17M3.5 17h17"/>
          </g>
        </svg>
        <span class="contact-text" style="top:294px">www.quarrybluelend,com</span>
      </li>
    </ul>

    <div class="silver-band"></div>
  </section>

</div>
</body>
</html>
```